Infographic - 360 degree feedback

We require an infographic design for a product/service offering called 360 degree feedback. The purpose of the infographic is to summarise what 360 degree feedback is as well as entice the prospective client to enquire about the product/service.
Target Market(s)
Government, council and commercial industry sectors
Industry/Entity Type
Recruitment
Font styles to use
Serif
Sans Serif
Colors
Designer to choose colors to be used in the design.
Requirements
Must have
- Color, simple, to the point and summarise the key points of the service offering

```html
<!DOCTYPE html>
<html lang="en">
<head>
<meta charset="utf-8">
<title>360 Degree Feedback – Quillmoor Advisory</title>
<link href="https://fonts.googleapis.com/css2?family=Arvo:wght@700&family=Oswald:wght@500&family=Roboto:wght@400;700&display=swap" rel="stylesheet">
<style>
  :root{
    --navy:#2a3770;
    --blue:#3d7cc2;
    --blue-light:#5b95d2;
    --paper:#f3f3f8;
    --ink:#2a3770;
    --yellow:#f4bc2c;
    --green:#6cbf3a;
    --white:#ffffff;
    --backdrop:#e7e7ec;
  }
  *{box-sizing:border-box;margin:0;padding:0}
  html,body{width:1200px;height:1200px;overflow:hidden}
  body{background:var(--backdrop);font-family:"Roboto",Arial,sans-serif;color:var(--ink);position:relative}

  .flyer{position:absolute;left:200px;top:40px;width:800px;height:1120px;background:var(--paper);overflow:hidden;box-shadow:0 6px 24px rgba(0,0,0,.15)}
  .flyer > *{position:absolute}

  .top-strip{left:0;top:0;width:800px;height:36px;background:var(--navy)}
  .title-banner{left:0;top:60px;width:540px;height:92px;background:var(--navy);color:var(--white);padding:12px 30px}
  .title-kicker{font-family:"Arvo",Georgia,serif;font-weight:700;font-size:18px}
  .title-main{font-family:"Arvo",Georgia,serif;font-weight:700;font-size:40px;line-height:1.1}
  .hero-art{left:570px;top:44px;width:190px;height:190px;border-radius:50%;background:radial-gradient(circle,#a9c9b4,#7fae9a)}

  .intro{left:30px;top:170px;width:520px;font-size:13px;line-height:1.45}
  .intro p{margin-bottom:8px}
  .intro .footnote{font-size:10px;font-style:italic}

  .benefits-band{left:0;top:312px;width:800px;height:330px;background:var(--blue)}
  .benefits-question{left:30px;top:334px;width:330px;font-family:"Oswald",Impact,sans-serif;font-weight:500;font-size:19px;line-height:1.25;color:var(--white);text-transform:uppercase}
  .benefits-art{left:30px;top:412px;width:330px;height:170px;border-radius:8px;background:linear-gradient(135deg,#5b95d2,#8fb4c9)}

  .benefit-list{left:390px;top:334px;width:380px;list-style:none}
  .benefit{display:flex;gap:14px;margin-bottom:16px;color:var(--white)}
  .benefit-icon{flex:0 0 44px;height:44px;border-radius:50%;background:var(--white)}
  .benefit-icon.is-yellow{background:var(--yellow)}
  .benefit h3{font-family:"Oswald",Impact,sans-serif;font-weight:500;font-size:14px;letter-spacing:.3px;text-transform:uppercase}
  .benefit p{font-size:10.5px;line-height:1.35;opacity:.92}

  .types-heading{left:0;top:652px;width:800px;text-align:center;font-family:"Oswald",Impact,sans-serif;font-weight:500;font-size:18px;text-transform:uppercase}
  .types-art{left:345px;top:686px;width:110px;height:110px;border-radius:50%;background:radial-gradient(circle,#ffffff,#b9cbe6);border:4px solid var(--blue-light)}

  .instrument{top:676px;width:290px}
  .instrument.normative{left:30px}
  .instrument.competency{left:480px}
  .instrument h3{display:inline-block;background:var(--navy);color:var(--white);font-family:"Oswald",Impact,sans-serif;font-weight:500;font-size:15px;padding:6px 14px;text-transform:uppercase;margin-bottom:10px}
  .instrument ul{list-style:none}
  .instrument li{display:flex;align-items:flex-start;gap:8px;font-size:11.5px;line-height:1.3;margin-bottom:5px}
  .tick{flex:0 0 13px;width:13px;height:13px;margin-top:1px}

  .process-heading{left:0;top:824px;width:800px;text-align:center;font-family:"Oswald",Impact,sans-serif;font-weight:500;font-size:18px;text-transform:uppercase}
  .step{width:126px;height:70px;padding:8px;font-size:10.5px;line-height:1.3;color:var(--white);background:var(--navy);display:flex;align-items:center;justify-content:center;text-align:center}
  .step.is-blue{background:var(--blue)}
  .step-1{left:30px;top:952px}
  .step-2{left:184px;top:929px}
  .step-3{left:338px;top:906px}
  .step-4{left:492px;top:883px}
  .step-5{left:646px;top:860px}
  .arrow{width:28px;height:14px}
  .arrow-1{left:156px;top:954px}
  .arrow-2{left:310px;top:931px}
  .arrow-3{left:464px;top:908px}
  .arrow-4{left:618px;top:885px}

  .closing-band{left:0;top:1036px;width:800px;height:84px;background:var(--navy);color:var(--white);padding:16px 30px;display:flex;justify-content:space-between;align-items:center}
  .closing-text{width:460px;font-size:13px;line-height:1.45}
  .brand{text-align:right}
  .brand-name{font-family:"Roboto",Arial,sans-serif;font-weight:700;font-size:19px;letter-spacing:1px;display:flex;align-items:center;gap:8px;justify-content:flex-end}
  .brand-mark{width:14px;height:14px;background:var(--white)}
  .brand-url{font-size:10px;margin-top:4px;opacity:.85}
</style>
</head>
<body>
<main class="flyer">
  <div class="top-strip"></div>

  <header class="title-banner">
    <div class="title-kicker">Introducing</div>
    <h1 class="title-main">360 Degree Feedback</h1>
  </header>
  <div class="hero-art" role="img" aria-label="Illustration of hands holding a magnifying glass, clock, trophy and checklist"></div>

  <section class="intro">
    <p>360 degree feedback is a powerful tool designed to assess individual, group and organisational performance, and most importantly, leadership behaviours.</p>
    <p>Designed in collaboration with Halden University, this 30 question short questionnaire provides you with the chance to compare the results of your staff to our normative sample* to ensure feedback is accurate.</p>
    <p class="footnote">*Normative sample consists of over 2600 Australian leaders from the general population.</p>
  </section>

  <div class="benefits-band"></div>
  <h2 class="benefits-question">What will the 360 degree feedback help me address and benefit my organisation?</h2>
  <div class="benefits-art" role="img" aria-label="Illustration of a manager at a desk with target, books and paper plane"></div>

  <ul class="benefit-list">
    <li class="benefit">
      <span class="benefit-icon is-yellow" role="img" aria-label="Leadership icon"></span>
      <div><h3>Leadership behaviours</h3><p>Crucial for maximising engagement in the organisation, research shows that an increase in engagement from your leaders correlates to an increase in productivity.</p></div>
    </li>
    <li class="benefit">
      <span class="benefit-icon" role="img" aria-label="Team icon"></span>
      <div><h3>Staff engagement</h3><p>Leadership behaviours have proven to be good predictors of staff engagement as it is a strong driver in engagement of human beings.</p></div>
    </li>
    <li class="benefit">
      <span class="benefit-icon is-yellow" role="img" aria-label="Research document icon"></span>
      <div><h3>Backed by research</h3><p>Quillmoor has partnered with Halden University to build a questionnaire based on 30 questions proven to be reliable in measuring leadership characteristics.</p></div>
    </li>
    <li class="benefit">
      <span class="benefit-icon" role="img" aria-label="Search for leaders icon"></span>
      <div><h3>Identify who your leaders are</h3><p>Our measurement tool will help you identify leaders who are strong in creating clarity in performance standards and provide reports which show key learnings amongst your group of leaders.</p></div>
    </li>
  </ul>

  <h2 class="types-heading">Types of 360 degree feedback instruments</h2>
  <div class="types-art" role="img" aria-label="Circular illustration of reports and charts"></div>

  <section class="instrument normative">
    <h3>Normative approach</h3>
    <ul>
      <li><svg class="tick" viewBox="0 0 13 13"><circle cx="6.5" cy="6.5" r="6.5" fill="#6cbf3a"/><path d="M3.5 6.8l2 2 4-4.2" stroke="#fff" stroke-width="1.6" fill="none"/></svg>Standard items</li>
      <li><svg class="tick" viewBox="0 0 13 13"><circle cx="6.5" cy="6.5" r="6.5" fill="#6cbf3a"/><path d="M3.5 6.8l2 2 4-4.2" stroke="#fff" stroke-width="1.6" fill="none"/></svg>Compare to a population of other leaders</li>
      <li><svg class="tick" viewBox="0 0 13 13"><circle cx="6.5" cy="6.5" r="6.5" fill="#6cbf3a"/><path d="M3.5 6.8l2 2 4-4.2" stroke="#fff" stroke-width="1.6" fill="none"/></svg>Known measurement quality</li>
      <li><svg class="tick" viewBox="0 0 13 13"><circle cx="6.5" cy="6.5" r="6.5" fill="#6cbf3a"/><path d="M3.5 6.8l2 2 4-4.2" stroke="#fff" stroke-width="1.6" fill="none"/></svg>Known reliability and validity (if well developed)</li>
    </ul>
  </section>

  <section class="instrument competency">
    <h3>Competency based</h3>
    <ul>
      <li><svg class="tick" viewBox="0 0 13 13"><circle cx="6.5" cy="6.5" r="6.5" fill="#6cbf3a"/><path d="M3.5 6.8l2 2 4-4.2" stroke="#fff" stroke-width="1.6" fill="none"/></svg>Locally adapted</li>
      <li><svg class="tick" viewBox="0 0 13 13"><circle cx="6.5" cy="6.5" r="6.5" fill="#6cbf3a"/><path d="M3.5 6.8l2 2 4-4.2" stroke="#fff" stroke-width="1.6" fill="none"/></svg>Focus on behaviours endorsed by the organisation</li>
      <li><svg class="tick" viewBox="0 0 13 13"><circle cx="6.5" cy="6.5" r="6.5" fill="#6cbf3a"/><path d="M3.5 6.8l2 2 4-4.2" stroke="#fff" stroke-width="1.6" fill="none"/></svg>Items to be assessed are chosen</li>
      <li><svg class="tick" viewBox="0 0 13 13"><circle cx="6.5" cy="6.5" r="6.5" fill="#6cbf3a"/><path d="M3.5 6.8l2 2 4-4.2" stroke="#fff" stroke-width="1.6" fill="none"/></svg>Linked to core competencies</li>
      <li><svg class="tick" viewBox="0 0 13 13"><circle cx="6.5" cy="6.5" r="6.5" fill="#6cbf3a"/><path d="M3.5 6.8l2 2 4-4.2" stroke="#fff" stroke-width="1.6" fill="none"/></svg>Strong face validity</li>
    </ul>
  </section>

  <h2 class="process-heading">How to start a 360 degree process</h2>
  <div class="step step-1">Whether normative or competency based, we need engagement</div>
  <svg class="arrow arrow-1" viewBox="0 0 28 14"><path d="M0 7h20M16 2l7 5-7 5" stroke="#2a3770" stroke-width="2" fill="none"/></svg>
  <div class="step step-2 is-blue">Get everyone together and set a destination. What will the outcomes be?</div>
  <svg class="arrow arrow-2" viewBox="0 0 28 14"><path d="M0 7h20M16 2l7 5-7 5" stroke="#2a3770" stroke-width="2" fill="none"/></svg>
  <div class="step step-3">Discuss the normative and competency based options</div>
  <svg class="arrow arrow-3" viewBox="0 0 28 14"><path d="M0 7h20M16 2l7 5-7 5" stroke="#2a3770" stroke-width="2" fill="none"/></svg>
  <div class="step step-4 is-blue">Choose the appropriate approach</div>
  <svg class="arrow arrow-4" viewBox="0 0 28 14"><path d="M0 7h20M16 2l7 5-7 5" stroke="#2a3770" stroke-width="2" fill="none"/></svg>
  <div class="step step-5">Set up a governance structure</div>

  <footer class="closing-band">
    <p class="closing-text">Quillmoor has best practice instruments for both types of 360 degree feedback and will advise you on the best way to start and manage your 360 project.</p>
    <div class="brand">
      <div class="brand-name"><span class="brand-mark"></span>QUILLMOOR ADVISORY</div>
      <div class="brand-url">www.quillmooradvisory.com.au</div>
    </div>
  </footer>
</main>
</body>
</html>
```